Language School website design

Harborline Languages is looking for a designer who can "spice up" our website under development with a new cascading style sheet (CSS) and re-design our logo and start branding for business cards etc.
It will be up to the designer to come up with a layout in photoshop that pleases the team after agreement on the static photoshop file, provide a CSS file and all needed objects in a ZIP file
The designer is to deliver a CSS that doesn't require changes to the HTML content or structure. You are to base the design and get input on title length and structure of the site on
www.harborline-languages.example.
Please refer to the contents of the various pages for developing the CSS file.
If we are happy with the work, we will use the designer for brochure design, branding, etc.
Updates

Project Deadline Extended
Reason: Programming was delayed, but design is now urgent.

Project Deadline Extended
Reason: Programmer delayed in finishing programming

Please send all information to martin@harborline-languages.example

A design we like is www.vostrel.example

Blue is a main colour on the site.

We will provide our photos and PDFs

Thanks

Target Market(s)

Spanish speaking companies

Industry/Entity Type

Business

Requirements
Should not have
• Old style fonts. Use of people in a classroom.

```html
<!DOCTYPE html>
<html lang="en">
<head>
<meta charset="utf-8">
<title>Harborline Languages – ACE English Courses</title>
<link rel="stylesheet" href="https://fonts.googleapis.com/css2?family=Oswald:wght@400&family=Noto+Serif:wght@400;700&family=Noto+Sans:wght@400;600&display=swap">
<style>
:root{
  --page-bg:#e4e4e4;
  --sheet:#ffffff;
  --brand-blue:#0a8fcc;
  --box-blue:#35a6d6;
  --navy:#13294b;
  --text:#1f1f1f;
  --muted:#3a3a3a;
  --rule:#cfcfcf;
}
*{margin:0;padding:0;box-sizing:border-box}
html,body{width:1200px;height:1200px;overflow:hidden}
body{background:var(--page-bg) repeating-linear-gradient(45deg,#dcdcdc 0 1px,transparent 1px 4px);font-family:"Noto Sans",Tahoma,sans-serif;color:var(--text);position:relative}
.sheet{position:absolute;left:120px;top:0;width:960px;height:1200px;background:var(--sheet);box-shadow:0 0 6px rgba(0,0,0,.25)}
.abs{position:absolute}
.lang-switch{right:10px;top:7px;font-size:11px;color:var(--muted)}
.top-rule{left:10px;right:10px;top:30px;height:1px;background:var(--rule)}
.brand{left:92px;top:74px;display:flex;align-items:center;gap:10px;font-family:"Noto Sans",sans-serif;font-size:20px;color:var(--navy)}
.brand-mark{width:22px;height:22px;background:var(--brand-blue)}
.main-nav{left:370px;top:89px;width:580px;height:32px;background:var(--brand-blue);display:flex;align-items:center;justify-content:space-between;padding:0 19px;font-family:"Noto Serif",serif;font-size:12.5px;color:#fff}
.main-nav span.arrow::before{content:"›";font-size:11px;margin-right:9px;opacity:.85}
.page-title{right:10px;top:154px;font-family:"Oswald",sans-serif;font-weight:400;font-size:26px;line-height:34px;color:var(--navy);letter-spacing:-.3px}
.intro{left:370px;top:205px;width:580px;font-size:11.4px;line-height:14.4px;text-align:justify;color:var(--text)}
.intro p{margin-bottom:14.4px}
.contact-bubble{left:96px;top:210px}
.bubble-text{left:110px;top:236px;width:152px;font-family:"Noto Serif",serif;font-size:11.6px;line-height:14.6px;color:#fff}
.bubble-text .phone{display:block;padding-left:19px}
.info-box{left:10px;width:275px;height:100px;background:var(--box-blue);color:#fff;font-family:"Noto Serif",serif;padding:7px 10px}
.info-box h3{font-size:12.5px;font-weight:700;margin-bottom:13px}
.info-box p{font-size:12.5px;line-height:14.6px}
.claim{right:400px;top:425px;text-align:right;font-family:"Noto Serif",serif;font-size:23px;line-height:29px;color:var(--navy)}
.photo{width:180px;height:133px;box-shadow:0 18px 14px -10px rgba(0,0,0,.22)}
.card-title{font-size:12px;font-weight:600;color:var(--brand-blue)}
.card-text{font-size:10.8px;line-height:14px;color:var(--text);width:180px}
.ph-phones{background:linear-gradient(160deg,#a9cfe6,#3d86b8 60%,#1f5a8a)}
.ph-tailor{background:linear-gradient(150deg,#6a6c70,#2a2c33 60%,#1c1d22)}
.ph-yacht{background:linear-gradient(180deg,#cfe3f1 0,#9ec6e2 55%,#3b6f9c 100%)}
.ph-port{background:linear-gradient(180deg,#d7e8f4 0,#a3c6df 45%,#9a5a3c 80%,#4e7ea0 100%)}
.ph-build{background:linear-gradient(180deg,#2f78b8 0,#7fb3dc 70%,#355b7e 100%)}
.ph-gears{background:radial-gradient(circle at 50% 45%,#7fc3e6,#1d5c8c 70%,#0e2f4d)}
.ph-finance{background:linear-gradient(160deg,#d6ecf9,#5aa6d8 55%,#1f5f98)}
.footer-rule{left:10px;right:10px;top:910px;height:4px;background:var(--brand-blue)}
.footer-info{left:10px;top:922px;font-size:11px;color:var(--muted)}
.footer-links{right:10px;top:922px;font-size:11px;color:var(--muted)}
</style>
</head>
<body>
<div class="sheet">
  <div class="abs lang-switch">Spanish | English | Catalan</div>
  <div class="abs top-rule"></div>

  <div class="abs brand"><span class="brand-mark"></span>Harborline Languages</div>

  <nav class="abs main-nav">
    <span>Home</span><span class="arrow">ACE! Classes</span><span class="arrow">ACE! Training</span><span class="arrow">Translations</span><span class="arrow">ACE! Club</span><span class="arrow">Contact</span>
  </nav>

  <h1 class="abs page-title">ACE English Courses</h1>

  <div class="abs intro">
    <p>Harborline Languages brings you... ACE -Applied Communication in English, courses designed for your industry and tailored to your company's needs. Say ACE to our specifically-designed English courses adapted to your industry: Yachting. Maritime. Finance. Engineering. Construction.</p>
    <p>In your company, at the time best suited to you, on the dates you want, and with the contents you choose. English adapted to your company. Face-to-face classes, telephone sessions, or both. What's more, our professional development department offers intensive English for Business courses and industry-specific courses.</p>
    <p>Our team of teachers are all native speakers and fully-qualified, as well as being experts in your industry. And if you need translations, our team of specialists can help you.</p>
    <p>Your sector, Your team, Your English goals</p>
  </div>

  <svg class="abs contact-bubble" width="170" height="165" viewBox="0 0 170 165" aria-hidden="true">
    <ellipse cx="84" cy="51" rx="83" ry="50" fill="#0a8fcc"/>
    <ellipse cx="51" cy="122" rx="26" ry="16" fill="#0a8fcc"/>
    <ellipse cx="26" cy="152" rx="12" ry="7" fill="#0a8fcc"/>
  </svg>
  <div class="abs bubble-text">Contact Harborline Languages every working day in Barcelona on:<span class="phone">+34 931 555 014</span></div>

  <div class="abs info-box" style="top:420px">
    <h3>CLASES PRESENCIALES</h3>
    <p>In-company, a la hora que te vaya mejor,<br>en las fechas que más te convengan,<br>y con los contenidos que tú elijas.</p>
  </div>
  <div class="abs info-box" style="top:530px">
    <h3>CURSOS MONOGRAFICOS</h3>
    <p>Dirigidos a profesionales que<br>deseen profundizar ciertos aspectos<br>del idioma inglés.</p>
  </div>

  <div class="abs claim">Profesores<br>nativos y<br>titulados, además<br>de ser expertos<br>en tu sector.</div>

  <div class="abs photo ph-phones" style="left:580px;top:420px" role="img" aria-label="Photo of telephone booths in a bright blue office"></div>
  <div class="abs card-title" style="left:581px;top:582px">SESIONES TELEFÓNICAS.</div>
  <div class="abs card-text" style="left:579px;top:603px">¡Aprende el idioma cuando quieras y desde donde quier</div>

  <div class="abs photo ph-tailor" style="left:770px;top:420px" role="img" aria-label="Photo of tailoring tools, tape measure and scissors on dark fabric"></div>
  <div class="abs card-title" style="left:771px;top:582px">A MEDIDA.</div>
  <div class="abs card-text" style="left:770px;top:603px">Diseñaremos aquello que mejor se adapte a vuestro perfil</div>

  <div class="abs photo ph-yacht" style="left:10px;top:650px" role="img" aria-label="Photo of a sailing yacht at sea"></div>
  <div class="abs card-title" style="left:10px;top:800px">YACHTING.</div>
  <div class="abs card-text" style="left:9px;top:821px">Para el sector náutico-deportivo</div>

  <div class="abs photo ph-port" style="left:200px;top:650px" role="img" aria-label="Photo of a crane loading shipping containers at a port"></div>
  <div class="abs card-title" style="left:200px;top:800px">MARITIME.</div>
  <div class="abs card-text" style="left:199px;top:821px">Para el sector marítimo y naval</div>

  <div class="abs photo ph-build" style="left:390px;top:650px" role="img" aria-label="Photo of building scaffolding against a blue sky"></div>
  <div class="abs card-title" style="left:390px;top:800px">CONSTRUCTION.</div>
  <div class="abs card-text" style="left:389px;top:821px">Para el sector de la construcción</div>

  <div class="abs photo ph-gears" style="left:580px;top:650px" role="img" aria-label="Illustration of interlocking blue gears"></div>
  <div class="abs card-title" style="left:580px;top:800px">ENGINEERING.</div>
  <div class="abs card-text" style="left:579px;top:821px">Para el sector de la ingeniería</div>

  <div class="abs photo ph-finance" style="left:770px;top:650px" role="img" aria-label="Illustration of financial charts and coin stacks over skyscrapers"></div>
  <div class="abs card-title" style="left:770px;top:800px">FINANCE.</div>
  <div class="abs card-text" style="left:769px;top:821px">Para el sector económico-<br>nanciero</div>

  <div class="abs footer-rule"></div>
  <div class="abs footer-info">Harborline Languages – www.harborline-languages.example – info@harborline-languages.example – T: 931 555 014</div>
  <div class="abs footer-links">Legal | Privacy | About us | FAQ</div>
</div>
</body>
</html>
```